Business card design for web travel company

Hi
we'd like to receive some proposal for a business card design.
Stayvano is a private travel club, dedicated to all travel lovers, with unique offers for exclusive destinations all around the world. At Stayvano you can find a wide range of offers for resorts, boutique hotels and travel packages at the best guaranteed price available on the market. The convenience of the offer is guaranteed by a private sales model: offers are available for a limited time only and they are personally chosen by Stayvano's qualified team of travel experts.
We offer only exclusive hotels with discounted prices but we are not an outlet or a discount supermarket: the design should reflect our connection with luxury, exclusivity using the same style of our website www.stayvano-example.com.
We want to make sure that when we'll present ourself to our business partner they will feel immediately which is our brand positioning giving them also a sense of an affordable and reliable partner.
In attachment you can also find our brand guidelines (please note that we are NOT USING ANY MORE THE TAG LINE "Five star outlet" mentioned in it).
The info to be inserted are:
Name Surname
Job Title
Tel
Mobile (when needed)
Email
Stayvano S.r.l.
Via Bruno Lesta 27
20131 Milano

```html
<!DOCTYPE html>
<html lang="en">
<head>
<meta charset="UTF-8">
<title>Stayvano — Business Card</title>
<link rel="stylesheet" href="https://fonts.googleapis.com/css2?family=Carlito:wght@400;700&display=swap">
<style>
  :root {
    --page: #ffffff;
    --card: #0c0e11;
    --stripe: rgba(255, 255, 255, 0.025);
    --band-bright: #ff00ff;
    --band-mid: #d400d4;
    --band-deep: #6e0a70;
    --gold-text: #cdb980;
    --gold-light: #f4ee7a;
    --gold-mid: #d6cc2a;
    --gold-deep: #8f8a12;
    --brand-white: #ffffff;
    --plate-dark: #030303;
    --plate-edge: #1d1a08;
  }
  * { box-sizing: border-box; margin: 0; padding: 0; }
  html, body {
    width: 1200px;
    height: 900px;
    overflow: hidden;
    background: var(--page);
  }
  .sheet {
    position: relative;
    width: 1200px;
    height: 900px;
  }
  .card {
    position: absolute;
    top: 295px;
    width: 544px;
    height: 310px;
    background:
      repeating-linear-gradient(60deg, transparent 0 7px, var(--stripe) 7px 9px),
      var(--card);
    box-shadow: 0 0 6px rgba(0, 0, 0, 0.35);
    overflow: hidden;
  }
  .card--front { left: 30px; }
  .card--back { left: 627px; }

  .band {
    position: absolute;
    left: 0;
    top: 115px;
    width: 100%;
    height: 80px;
  }
  .card--front .band {
    background: linear-gradient(90deg, var(--band-bright) 0%, var(--band-bright) 70%, var(--band-mid) 100%);
  }
  .card--back .band {
    background: linear-gradient(90deg, var(--band-bright) 0%, var(--band-deep) 30%, var(--band-deep) 70%, var(--band-bright) 100%);
    display: flex;
    flex-direction: column;
    align-items: center;
    justify-content: center;
    gap: 4px;
  }
  .contact-line {
    font-family: "Carlito", "Calibri", sans-serif;
    font-size: 15px;
    line-height: 18px;
    color: var(--gold-text);
    letter-spacing: 0.2px;
    white-space: nowrap;
  }
  .contact-line .sep { margin: 0 6px; }

  .person {
    position: absolute;
    left: 0;
    top: 52px;
    width: 100%;
    text-align: center;
    font-family: "Carlito", "Calibri", sans-serif;
    color: var(--gold-text);
  }
  .person__name {
    font-size: 20px;
    font-weight: 700;
    letter-spacing: 0.6px;
  }
  .person__role {
    margin-top: 4px;
    font-size: 14px;
    letter-spacing: 1.4px;
    text-transform: uppercase;
  }

  .brand-plate {
    position: absolute;
    left: 52px;
    top: 28px;
    width: 438px;
    height: 254px;
  }
  .brand-name {
    position: absolute;
    left: 52px;
    top: 28px;
    width: 438px;
    height: 254px;
    display: flex;
    align-items: center;
    justify-content: center;
    font-family: "Carlito", "Calibri", sans-serif;
    font-size: 64px;
    font-weight: 400;
    color: var(--brand-white);
    letter-spacing: 2px;
  }
</style>
</head>
<body>
  <main class="sheet">
    <section class="card card--front" aria-label="Business card front">
      <div class="band"></div>
      <svg class="brand-plate" viewBox="0 0 438 254" aria-hidden="true">
        <defs>
          <radialGradient id="plate-fill" cx="50%" cy="50%" r="62%">
            <stop offset="0%" stop-color="var(--plate-dark)"/>
            <stop offset="75%" stop-color="var(--plate-dark)"/>
            <stop offset="100%" stop-color="var(--plate-edge)"/>
          </radialGradient>
          <linearGradient id="plate-rim" x1="0" y1="0" x2="1" y2="1">
            <stop offset="0%" stop-color="var(--gold-light)"/>
            <stop offset="50%" stop-color="var(--gold-mid)"/>
            <stop offset="100%" stop-color="var(--gold-deep)"/>
          </linearGradient>
        </defs>
        <rect x="22" y="20" width="394" height="214" rx="34"
              fill="url(#plate-fill)" stroke="url(#plate-rim)" stroke-width="5"/>
      </svg>
      <div class="brand-name">Stayvano</div>
    </section>

    <section class="card card--back" aria-label="Business card back">
      <div class="person">
        <p class="person__name">Giulia Ferraro</p>
        <p class="person__role">Partnership Manager</p>
      </div>
      <div class="band">
        <p class="contact-line">Stayvano S.r.l., Via Bruno Lesta 27, 20131 Milano</p>
        <p class="contact-line">T. 02 8846 1173<span class="sep">•</span>M. 3401928576</p>
        <p class="contact-line">E. stayvano@example-mail.com</p>
      </div>
    </section>
  </main>
</body>
</html>
```